Striking new Advert required for Commercial Real Estate Agency

We need a a NEW newspaper advertisement for the marketing of a large commercial property (a Backpackers lodge)

Dimensions are to be width of 101mm and height of 100mm (10cms)

Our key design statement for this advert is clean, modern and minimalist design, with accents of 'HOT PINK' colour to remove it from looking too boring, perhaps in the area of the contact icons. The heirachy of the advert is outlined in the attached ADVERTISEMENT TEXT FILE.

Our company name is THE VANTREL COLLECTIVE, and we want our brand to appear professional yet classy in it's design style (sort of like an advertising or design agency)

We have two logo options below, one more square in its layout (which we prefer) and the other more rectangular, which may be better suited for the layout. We are not adverse to the logo being reversed (white text on black), along with other key element areas such as the main advert heading and the "FOR SALE" part, and think this would be a good option.
There are two photos attached to be included in the advert.

We have attached an example of an old advert that we did, which we DID NOT LIKE, and which was for a smaller width than the one we need (it is only 65% of the width of this one). WE have also atached a file showing layout of some of our competitors adverts, which we dont think are too good either.

We are really open for ideas, but have time pressures, so please come back with any questions as soon as you can, if needed.

Thank you
Updates

Thank you for the great and diverse designs. There are a few standout options, but one style that we prefer most.

Target Market(s)

We are wanting this newspaper advertisement to attract interest from real estat e developers, investors and motel/lodge owners, along with other high nett worth individuals

Industry/Entity Type

Real Estate

Font styles to use
Serif
Sans Serif

Colors
1b1b1b
a54499
474747
fbfbfb

Requirements
Must have
• Clean modern look, predominantly monochromatic or black and white, with the hot pink accent somewhere, as mentioned above.
• All the contents of the TEXT provided, perhaps with additional space to add a little more if needed, Please advise if you think we dont have enough space for all of the TEXT
Should not have
• Script like fonts
• Cartoonish characters
• a 'cheap' look

```html
<!DOCTYPE html>
<html lang="en">
<head>
<meta charset="utf-8">
<title>For Sale – Kestrel Hill Land Grab</title>
<link rel="stylesheet" href="https://fonts.googleapis.com/css2?family=Montserrat:wght@300;400;800&family=Source+Sans+3:wght@300;400;600;700&display=swap">
<style>
  :root {
    --ink: #1b1b1b;
    --pink: #a54499;
    --slate: #474747;
    --paper: #ffffff;
    --mist: #f1f1f1;
    --stone: #8f8f8f;
    --photo-sky: #7fa6d6;
    --photo-wall: #e4e6ea;
    --photo-green: #5d7a3a;
  }
  html, body { margin: 0; padding: 0; }
  body {
    width: 1200px; height: 903px; overflow: hidden;
    background: #e9e9e9;
    font-family: "Source Sans 3", sans-serif;
    color: var(--ink);
  }
  .advert {
    position: absolute; left: 160px; top: 16px;
    width: 786px; height: 777px;
    transform: scale(1.12); transform-origin: top left;
    background: var(--paper);
  }
  .property-photo {
    position: absolute; left: 36px; top: 32px; width: 396px; height: 398px;
    background: linear-gradient(160deg, var(--photo-sky) 0%, #b9cde6 30%, var(--photo-wall) 48%, #cfd2d8 65%, var(--photo-green) 85%, #3f5a2a 100%);
  }
  .sale-banner {
    position: absolute; left: 446px; top: 32px; width: 302px; height: 67px;
    background: var(--pink); color: #fff;
    font-family: "Montserrat", sans-serif; font-weight: 800; font-size: 47px;
    display: flex; align-items: center; justify-content: center; letter-spacing: 0.5px;
  }
  .tagline {
    position: absolute; left: 446px; top: 108px; width: 302px; text-align: center;
    font-weight: 300; font-size: 24px; color: var(--slate);
  }
  .address-block {
    position: absolute; left: 446px; top: 160px; width: 302px; height: 106px;
    background: var(--stone); color: #fff;
    font-family: "Montserrat", sans-serif; font-weight: 300; font-size: 23px; line-height: 30px;
    display: flex; align-items: center; justify-content: center; text-align: center;
  }
  .teaser {
    position: absolute; left: 446px; top: 292px; width: 306px;
    font-weight: 300; font-size: 21px; line-height: 27px; color: var(--ink);
  }
  .tender-note {
    position: absolute; left: 446px; top: 370px; width: 302px; height: 49px;
    background: var(--mist); color: var(--pink);
    font-weight: 600; font-size: 21px;
    display: flex; align-items: center; justify-content: center;
  }
  .key-details {
    position: absolute; left: 0; top: 438px; width: 786px; height: 233px;
    background: var(--mist); box-sizing: border-box; padding: 3px 38px 0 37px;
  }
  .key-details h2 {
    margin: 0; font-weight: 700; font-size: 20px; line-height: 26px;
  }
  .key-details ul { margin: 2px 0 0; padding: 0; list-style: none; }
  .key-details li {
    position: relative; padding-left: 33px; margin-bottom: 7px;
    font-weight: 300; font-size: 20.5px; line-height: 26px; text-align: justify; color: var(--ink);
  }
  .key-details li::before {
    content: ""; position: absolute; left: 9px; top: 11px;
    width: 8px; height: 8px; border-radius: 50%; background: var(--pink);
  }
  .key-details sup { font-size: 11px; line-height: 0; }
  .contact-bar {
    position: absolute; left: 0; top: 671px; width: 786px; height: 106px;
    background: var(--ink); color: #fff;
  }
  .agent-name {
    position: absolute; left: 36px; top: 2px; font-weight: 600; font-size: 22px;
  }
  .contact-line {
    position: absolute; display: flex; align-items: center; gap: 10px;
    font-weight: 400; font-size: 20px;
  }
  .contact-line svg { width: 16px; height: 16px; flex: none; }
  .brand-mark {
    position: absolute; left: 580px; top: 20px; display: flex; align-items: center; gap: 12px;
  }
  .brand-mark .brand-square { width: 14px; height: 14px; background: var(--pink); }
  .brand-mark .brand-name {
    font-family: "Montserrat", sans-serif; font-weight: 400; font-size: 17px; line-height: 20px;
    color: #fff; letter-spacing: 1px; width: 130px;
  }
</style>
</head>
<body>
  <main class="advert">
    <div class="property-photo" role="img" aria-label="Photo of the white two-storey weatherboard lodge with bay window and fire escape, garden in front, blue sky above"></div>

    <div class="sale-banner">FOR SALE</div>
    <div class="tagline">Kestrel Hill Land Grab</div>
    <div class="address-block">Corwen's Lodge,<br>27 Harcourt Street,<br>Kestrel Hill</div>
    <p class="teaser" style="margin:0">This Old Beauty has served many, and is now ripe for development.</p>
    <div class="tender-note">Now Selling by Closed Tender</div>

    <section class="key-details">
      <h2>One of Kestrel Hill's largest land areas, now offered with vacant possession, with key details being:</h2>
      <ul>
        <li>Large Land area of 2076m<sup>2</sup> with elevated sunny position and great outlook + access from Penrose Street</li>
        <li>Existing Backpackers Lodge of 970m<sup>2</sup> providing multiple rooms with amenity areas</li>
        <li>Four adjacent sites also available, taking total land area to 4452m<sup>2</sup>, an unprecedented Land Offering in this popular cuity fringe location</li>
      </ul>
    </section>

    <footer class="contact-bar">
      <div class="agent-name">Miles Arundel</div>
      <div class="contact-line" style="left:36px; top:34px;">
        <svg viewBox="0 0 16 16"><path d="M3 1.5 L5.8 1.5 L6.8 5 L5 6.3 C5.9 8.2 7.6 9.9 9.6 10.9 L10.9 9.2 L14.5 10.2 L14.5 13 C14.5 14 13.6 14.6 12.6 14.5 C6.6 13.8 2.2 9.4 1.5 3.4 C1.4 2.4 2 1.5 3 1.5 Z" fill="none" stroke="#a54499" stroke-width="1.4"/></svg>
        <span>(04) 555 0142</span>
      </div>
      <div class="contact-line" style="left:36px; top:62px;">
        <svg viewBox="0 0 16 16"><rect x="4" y="1" width="8" height="14" rx="1.5" fill="none" stroke="#a54499" stroke-width="1.4"/><circle cx="8" cy="12.3" r="0.9" fill="#a54499"/></svg>
        <span>(021) 555 018</span>
      </div>
      <div class="contact-line" style="left:230px; top:30px;">
        <svg viewBox="0 0 16 16"><rect x="2" y="4" width="12" height="8" fill="#a54499"/><path d="M2 4 L8 9 L14 4" fill="none" stroke="#1b1b1b" stroke-width="1.2"/></svg>
        <span>miles@vantrelcollective.co.nz</span>
      </div>
      <div class="contact-line" style="left:230px; top:58px;">
        <svg viewBox="0 0 16 16"><g fill="none" stroke="#a54499" stroke-width="1.2"><circle cx="8" cy="8" r="6"/><ellipse cx="8" cy="8" rx="2.6" ry="6"/><line x1="2" y1="8" x2="14" y2="8"/></g></svg>
        <span>www.vantrelcollective.co.nz</span>
      </div>
      <div class="brand-mark">
        <span class="brand-square"></span>
        <span class="brand-name">THE VANTREL COLLECTIVE</span>
      </div>
    </footer>
  </main>
</body>
</html>
```